KORVELLA Corporate Business Card

Modern business card design for company which focuses in the areas of Staffing, IT Consulting & Data Services. Please note: We are no longer using the IT subscript on the logo. All designs should have IT subscript removed.
Website: www.korvellait.example

```html
<!DOCTYPE html>
<html lang="en">
<head>
<meta charset="utf-8">
<title>KORVELLA Business Card</title>
<link href="https://fonts.googleapis.com/css2?family=Lato:wght@400;700;900&display=swap" rel="stylesheet">
<style>
  :root {
    --stage: #2b2e33;
    --card: #07090b;
    --card-edge: #101316;
    --brand-blue: #1c9ce0;
    --text-white: #f2f4f6;
    --pattern-tone: #0e1114;
  }
  * { box-sizing: border-box; margin: 0; padding: 0; }
  html, body {
    width: 1200px; height: 900px; overflow: hidden;
    background: var(--stage);
    font-family: "Lato", sans-serif;
  }
  .canvas {
    width: 1200px; height: 900px;
    display: flex; flex-direction: column; align-items: center; justify-content: center;
    gap: 44px;
  }
  .card {
    position: relative;
    width: 630px; height: 360px;
    background: var(--card);
    border: 1px solid var(--card-edge);
    box-shadow: 0 10px 28px rgba(0,0,0,.45);
    overflow: hidden;
  }
  .wordmark {
    display: flex; align-items: center; gap: 10px;
    color: var(--brand-blue);
    font-weight: 900; letter-spacing: 1px;
  }
  .wordmark__square {
    width: 0.7em; height: 0.7em;
    background: var(--brand-blue);
    border-radius: 3px;
  }
  /* Front */
  .card--front .wordmark { position: absolute; left: 44px; top: 70px; font-size: 46px; }
  .contact-block { position: absolute; left: 330px; top: 150px; }
  .person__name { color: var(--brand-blue); font-weight: 700; font-size: 19px; letter-spacing: .5px; }
  .person__title { color: var(--brand-blue); font-size: 14px; margin-top: 2px; }
  .contact-list { list-style: none; margin-top: 14px; }
  .contact-list li {
    display: flex; align-items: center; gap: 8px;
    color: var(--text-white); font-size: 15px; line-height: 26px;
  }
  .contact-list svg { width: 14px; height: 14px; flex: none; }
  .address {
    position: absolute; left: 330px; top: 278px;
    color: var(--brand-blue); font-size: 15px; line-height: 21px;
  }
  .accent-dash {
    position: absolute; left: 78px; top: 300px;
    width: 12px; height: 3px; background: var(--brand-blue);
  }
  /* Back */
  .pattern-field {
    position: absolute; inset: 0;
    background: linear-gradient(135deg, var(--pattern-tone), var(--card) 60%, var(--pattern-tone));
  }
  .card--back .wordmark {
    position: absolute; left: 50%; top: 50%;
    transform: translate(-50%, -50%);
    font-size: 52px;
  }
</style>
</head>
<body>
<main class="canvas">
  <section class="card card--front">
    <div class="wordmark"><span class="wordmark__square"></span>KORVELLA</div>
    <div class="contact-block">
      <p class="person__name">DANIEL MERCER</p>
      <p class="person__title">Sales Manager</p>
      <ul class="contact-list">
        <li>
          <svg viewBox="0 0 16 16" aria-hidden="true"><circle cx="8" cy="8" r="7" fill="none" stroke="var(--brand-blue)" stroke-width="1.5"/><path d="M5.5 4.5l1.3 1.8-.8 1c.6 1.2 1.4 2 2.5 2.5l1-.8 1.8 1.3-.8 1.3c-2.8-.3-5.5-3-5.8-5.8z" fill="var(--brand-blue)"/></svg>
          555-014-2270
        </li>
        <li>
          <svg viewBox="0 0 16 16" aria-hidden="true"><rect x="1.5" y="3.5" width="13" height="9" fill="none" stroke="var(--brand-blue)" stroke-width="1.5"/><path d="M1.5 3.5L8 9l6.5-5.5" fill="none" stroke="var(--brand-blue)" stroke-width="1.5"/></svg>
          contact@korvellait.example
        </li>
        <li>
          <svg viewBox="0 0 16 16" aria-hidden="true"><circle cx="8" cy="8" r="6.5" fill="none" stroke="var(--brand-blue)" stroke-width="1.5"/><ellipse cx="8" cy="8" rx="2.8" ry="6.5" fill="none" stroke="var(--brand-blue)" stroke-width="1.2"/><path d="M1.5 8h13" stroke="var(--brand-blue)" stroke-width="1.2"/></svg>
          www.korvellait.example
        </li>
      </ul>
    </div>
    <p class="address">48 Alder Street<br>Riverton, ST 00000</p>
    <span class="accent-dash"></span>
  </section>

  <section class="card card--back">
    <div class="pattern-field" role="img" aria-label="Faint repeating brand pattern across the dark card back"></div>
    <div class="wordmark"><span class="wordmark__square"></span>KORVELLA</div>
  </section>
</main>
</body>
</html>
```